Luxury Lifestyle Website - Blog and Product Showcasing

I am looking to create a simple, yet elegant website where I can post blog posts and feature products and brand partnerships for my company, Velour Hollis. I want a very elegant but not overly complex site. I like the look and feel of Harriet Osborne's site - I don't need for it to be that robust or sophisticated, but that is the aesthetic I am going for. I would like to include my primary logo at the top of the main page, and also incorporate my alternative logos throughout the site in strategic places.

Target Market(s)

Luxury Brands; 20s-60s year olds; women; high-end fashion and tastes

Industry/Entity Type

Luxury Lifestyle - Blogging - Product Showcasing

Coding

Coded - Design and coding required

Number of Pages Required

4 page

Font styles to use
Sans Serif
Script
Other font styles liked:
• Pinyon

Colors
00AB8E
00BBA5
67D7C9
C6EFE9
E9F9F6
59FF00
82FF00
B8FF75
E3FFCB
F4FFEA

Requirements
Must have
• Creative use of my various logos. PASTEL GREENS or a DEEP DARK GREEN. Nothing bright, very soft and elegant.
Nice to have
• Elegant script that is easy to read.
Should not have
• Bright colors or overly modern look or feel.

```html
<!DOCTYPE html>
<html lang="en">
<head>
<meta charset="utf-8">
<title>Velour Hollis — Luxury Lifestyle</title>
<link href="https://fonts.googleapis.com/css2?family=Pinyon+Script&family=Lora:wght@400;500&family=Montserrat:wght@500;700&display=swap" rel="stylesheet">
<style>
:root{
  --teal:#00BBA5;
  --teal-deep:#00AB8E;
  --mint:#E6F7F3;
  --mint-soft:#E9F9F6;
  --ink:#2f3a3a;
  --text:#4a4f4f;
  --muted:#8d9494;
  --line:#e3e8e7;
  --gold:#d9a21c;
  --white:#ffffff;
}
*{box-sizing:border-box;margin:0;padding:0}
html,body{width:1200px;height:4724px;overflow:hidden}
body{position:relative;background:var(--white);font-family:'Lora',Georgia,serif;color:var(--text)}
.abs{position:absolute}
.script{font-family:'Pinyon Script',cursive;color:var(--ink);font-weight:400}
.label{font-family:'Montserrat',Arial,sans-serif;font-weight:700;letter-spacing:2px;text-transform:uppercase}
.photo{position:absolute}
.btn{position:absolute;display:flex;align-items:center;justify-content:center;background:var(--teal);color:var(--white);font-family:'Montserrat',Arial,sans-serif;font-weight:700;font-size:12px;letter-spacing:2.5px;text-transform:uppercase}

/* header */
.hero-band{top:0;left:0;width:1200px;height:558px;background:var(--mint)}
.menu{top:42px;left:104px;display:flex;align-items:center;gap:20px;font-size:12px;letter-spacing:1px;color:var(--ink)}
.menu svg{display:block}
.brand{top:20px;left:450px;width:300px;text-align:center;color:var(--ink)}
.brand .mark{width:30px;height:30px;border:1.5px solid #8a9290;margin:0 auto 6px}
.brand .name{font-size:16px;letter-spacing:2px;text-transform:uppercase}
.brand .tag{font-family:'Montserrat',sans-serif;font-size:6px;letter-spacing:3px;color:var(--muted);margin-top:2px}
.nav-right{top:46px;font-size:12px;letter-spacing:1px;color:var(--ink)}
.hero-photo{top:105px;left:99px;width:1018px;height:545px;background:linear-gradient(90deg,#ece3dc 0%,#e4d8cf 45%,#b99a82 65%,#e8ded6 100%)}
.hero-circle{top:186px;left:169px;width:392px;height:392px;border-radius:50%;background:var(--teal);color:var(--white);text-align:center}
.hero-circle .small{position:absolute;top:118px;width:100%;font-size:38px}
.hero-circle .big{position:absolute;top:160px;width:100%;font-size:50px}
.hero-circle .btn{top:248px;left:90px;width:210px;height:50px;background:var(--white);color:var(--teal);font-size:11px}

/* intro */
.intro-photo{top:765px;left:0;width:521px;height:633px;background:linear-gradient(160deg,#f1ede8 0%,#d9c8ba 50%,#efe9e3 100%)}
.intro-brand{top:818px;left:609px;font-size:18px;letter-spacing:2px;color:#777}
.intro-title{top:890px;left:609px;font-size:58px;line-height:58px}
.intro-copy{top:1050px;left:609px;width:460px;padding-left:48px;border-left:1px solid #cfd6d5;font-size:17px;line-height:30.5px;color:var(--text)}
.intro-flower{top:970px;left:1060px;width:140px;height:320px;background:radial-gradient(ellipse at 60% 50%,#e9eef0 0%,#f2f5f4 45%,rgba(255,255,255,0) 72%)}
.intro-btn{top:1310px;left:609px;width:210px;height:52px}

/* partners */
.partners-title{top:1505px;left:0;width:1200px;text-align:center;font-size:18px;letter-spacing:3px;color:var(--ink)}
.partner{top:1570px;background:#dde3ea}

/* products */
.products-band{top:1740px;left:0;width:1200px;height:686px;background:var(--mint)}
.section-title{left:0;width:1200px;text-align:center;font-size:66px;line-height:80px}
.card{top:1905px;width:280px;height:325px;background:var(--white)}
.card .item{position:absolute}
.card-name{top:2253px;width:280px;text-align:center;font-size:21px;line-height:29px;color:var(--ink)}
.rating{top:2322px;width:280px;display:flex;justify-content:center;align-items:center;gap:10px;font-family:'Montserrat',sans-serif;font-size:10px;color:var(--text)}
.rating .stars{color:var(--gold);letter-spacing:1px;font-size:11px}
.view-btn{top:148px;left:42px;width:196px;height:46px;font-size:11px}

/* videos */
.flower-left{top:2430px;left:0;width:150px;height:140px;background:radial-gradient(ellipse at 30% 50%,#e8eaf0 0%,#f2f4f5 45%,rgba(255,255,255,0) 72%)}
.video{top:2615px;height:372px}
.play{position:absolute;top:150px;left:244px;width:96px;height:96px}
.video-caption{top:3034px;left:300px;width:600px;text-align:center;font-size:21px;line-height:33px;color:var(--ink)}
.pager{top:3036px;font-style:italic;font-size:16px;color:var(--ink);display:flex;align-items:center;gap:18px}
.divider{top:3196px;left:0;width:1200px;height:1px;background:var(--line)}

/* articles */
.article-img{top:3354px;width:280px;height:279px}
.article-date{top:3664px;font-family:'Montserrat',sans-serif;font-size:10px;letter-spacing:2px;color:#9aa0a0}
.article-title{top:3694px;width:300px;font-size:22px;line-height:28px;color:var(--ink)}
.article-more{top:3800px;font-size:11px;color:var(--teal)}

/* instagram strip */
.insta{top:3997px;height:279px}

/* footer */
.footer-band{top:4276px;left:0;width:1200px;height:448px;background:var(--mint)}
.foot-brand{top:4368px;left:156px;width:140px;text-align:center;color:var(--ink)}
.foot-brand .mark{width:28px;height:28px;border:1.5px solid #8a9290;margin:0 auto 6px}
.foot-brand .name{font-size:14px;letter-spacing:2px;text-transform:uppercase}
.foot-brand .tag{font-family:'Montserrat',sans-serif;font-size:5.5px;letter-spacing:3px;color:var(--muted);margin-top:2px}
.foot-text{font-family:'Montserrat',sans-serif;font-size:12px;line-height:21px;color:var(--ink);font-weight:500}
.contact{display:flex;align-items:center;gap:16px}
.contact .dot{width:20px;height:20px;border-radius:50%;background:#d5ebe7;display:flex;align-items:center;justify-content:center}
.foot-head{font-size:16px;font-weight:500;color:var(--ink)}
.foot-links{top:4414px;left:498px;list-style:none}
.foot-links li{font-family:'Montserrat',sans-serif;font-size:12px;line-height:28px;color:var(--ink)}
.email{top:4474px;left:749px;width:238px;height:44px;background:var(--white);border:1px solid #d9e6e3;font-family:'Montserrat',sans-serif;font-size:12px;color:#9aa0a0;padding:14px 18px}
.social{top:4582px;left:749px;display:flex;gap:12px}
.social span{width:28px;height:28px;border-radius:50%;border:1px solid #b9c7c4}
.copyright{top:4676px;left:0;width:1200px;text-align:center;font-family:'Montserrat',sans-serif;font-size:11px;color:var(--ink)}
</style>
</head>
<body>

<!-- Header & hero -->
<div class="abs hero-band"></div>
<div class="abs menu">
  <svg width="30" height="20" viewBox="0 0 30 20"><g stroke="#2f3a3a" stroke-width="2"><line x1="0" y1="2" x2="30" y2="2"/><line x1="0" y1="10" x2="30" y2="10"/><line x1="0" y1="18" x2="30" y2="18"/></g></svg>
  <span>MENU</span>
</div>
<div class="abs brand">
  <div class="mark"></div>
  <div class="name">Velour Hollis</div>
  <div class="tag">LUXURY LIFESTYLE</div>
</div>
<div class="abs nav-right" style="left:988px">SEARCH</div>
<div class="abs nav-right" style="left:1082px">EN ▾</div>

<div class="photo hero-photo" role="img" aria-label="Portrait of a smiling woman with long wavy brown hair against a soft beige backdrop"></div>
<div class="abs hero-circle">
  <div class="small script" style="font-family:'Lora',serif;color:#fff">Welcome to</div>
  <div class="big" style="font-family:'Lora',serif">Velour Hollis.</div>
  <div class="btn">View Collections</div>
</div>

<!-- Intro -->
<div class="photo intro-photo" role="img" aria-label="Woman in a white tank top posing and smiling over her shoulder"></div>
<div class="abs intro-brand">Velour Hollis</div>
<h2 class="abs intro-title script">Its about way more<br>than just a pretty outfit.</h2>
<div class="photo intro-flower" role="img" aria-label="Soft watercolour floral sprig"></div>
<p class="abs intro-copy">Vivamus malesuada orci turpis, sit amet efficitur tortor varius sed. Morbi eu cursus erat. Donec vulputate ligula vitae quam semper, in tempus tellus ultrices. Praesent eget ligula ut odio gravida blandit sed ac neque. Pellentesque habitant morbi tristique senectus et netus et malesuada fames ac turpis egestas.</p>
<div class="btn intro-btn">Read More</div>

<!-- Partners -->
<div class="abs partners-title">BRAND PARTNERSHIPS</div>
<div class="abs partner" style="left:208px;width:90px;height:90px;border-radius:6px"></div>
<div class="abs partner" style="left:372px;top:1595px;width:175px;height:48px"></div>
<div class="abs partner" style="left:632px;width:94px;height:94px;border-radius:50%"></div>
<div class="abs partner" style="left:800px;top:1595px;width:190px;height:48px"></div>

<!-- Products -->
<div class="abs products-band"></div>
<h2 class="abs section-title script" style="top:1800px">My products</h2>

<div class="abs card" style="left:156px"><div class="item" role="img" aria-label="Sage green button-front sundress" style="left:75px;top:30px;width:130px;height:270px;background:linear-gradient(180deg,#a7bc98,#6f9460);border-radius:40% 40% 10% 10%"></div></div>
<div class="abs card" style="left:461px"><div class="item" role="img" aria-label="Beige short-sleeve button-front dress" style="left:70px;top:50px;width:140px;height:250px;background:linear-gradient(180deg,#e3d5aa,#c8b684);border-radius:30% 30% 8% 8%"></div></div>
<div class="abs card" style="left:765px">
  <div class="item" role="img" aria-label="Cream leather hobo handbag" style="left:78px;top:60px;width:124px;height:220px;background:linear-gradient(180deg,#f6ece6,#f1e2d9);border-radius:30% 30% 20% 20%"></div>
  <div class="btn view-btn">View Product</div>
</div>
<svg class="abs" style="top:2066px;left:1076px" width="12" height="18" viewBox="0 0 12 18"><polyline points="2,2 9,9 2,16" fill="none" stroke="#2f3a3a" stroke-width="1.6"/></svg>

<div class="abs card-name" style="left:156px">Massa a pharetra tortor<br>decenas</div>
<div class="abs card-name" style="left:461px">Massa a pharetra tortor<br>decenas</div>
<div class="abs card-name" style="left:765px">Massa a pharetra tortor<br>decenas</div>
<div class="abs rating" style="left:156px"><span class="stars">★★★★★</span>5 reviews</div>
<div class="abs rating" style="left:461px"><span class="stars">★★★★★</span>5 reviews</div>
<div class="abs rating" style="left:765px"><span class="stars">★★★★★</span>5 reviews</div>

<!-- Videos -->
<div class="photo flower-left" role="img" aria-label="Soft watercolour floral sprig"></div>
<h2 class="abs section-title script" style="top:2507px">Recent Videos</h2>
<div class="photo video" style="left:0;width:283px;background:linear-gradient(135deg,#d6d6d6,#9a9a9a 60%,#c8c8c8)" role="img" aria-label="Black and white portrait of a woman with wavy hair"></div>
<div class="photo video" style="left:308px;width:584px;background:linear-gradient(180deg,#d7d3cc 0%,#c4bdb3 60%,#8c6a4c 100%)" role="img" aria-label="Woman sitting on a wooden floor beside a large marquee ampersand">
  <svg class="play" viewBox="0 0 96 96"><circle cx="48" cy="48" r="44" fill="rgba(255,255,255,0.15)" stroke="#fff" stroke-width="3"/><polygon points="38,30 68,48 38,66" fill="none" stroke="#fff" stroke-width="3"/></svg>
</div>
<div class="photo video" style="left:917px;width:283px;background:linear-gradient(135deg,#cfcfcf,#8f8f8f 60%,#d0d0d0)" role="img" aria-label="Black and white image of a woman at a computer monitor"></div>

<div class="abs pager" style="left:108px"><svg width="32" height="10" viewBox="0 0 32 10"><polyline points="6,1 1,5 6,9" fill="none" stroke="#2f3a3a"/><line x1="1" y1="5" x2="32" y2="5" stroke="#2f3a3a"/></svg>Prev</div>
<p class="abs video-caption">Massa a pharetra tortor decenas metus magna sed ultricies tempus...</p>
<div class="abs pager" style="left:1007px">Next<svg width="32" height="10" viewBox="0 0 32 10"><line x1="0" y1="5" x2="31" y2="5" stroke="#2f3a3a"/><polyline points="26,1 31,5 26,9" fill="none" stroke="#2f3a3a"/></svg></div>
<div class="abs divider"></div>

<!-- Articles -->
<h2 class="abs section-title script" style="top:3252px">Latest Articles</h2>
<div class="photo article-img" style="left:130px;background:linear-gradient(135deg,#3e6f8c,#c49a6a 55%,#6b4b30)" role="img" aria-label="Woman shopping in a boutique"></div>
<div class="photo article-img" style="left:459px;background:linear-gradient(180deg,#c63a2c,#e2602f 45%,#c9c2b8)" role="img" aria-label="Person with a woven net bag on red stairs"></div>
<div class="photo article-img" style="left:791px;background:linear-gradient(180deg,#3a3a3a,#8a8a8a 60%,#e2e2e2)" role="img" aria-label="Models walking a fashion runway"></div>

<div class="abs article-date" style="left:130px">29 SEPTEMBER, 2020</div>
<div class="abs article-date" style="left:459px">29 SEPTEMBER, 2020</div>
<div class="abs article-date" style="left:791px">29 SEPTEMBER, 2020</div>
<h3 class="abs article-title" style="left:130px;font-weight:400">Aenean non semper ante. Phasellus dapibus placerat suscipit...</h3>
<h3 class="abs article-title" style="left:459px;font-weight:400">Massa, a pharetra tortor. Maecenas metus magna sed ultricies tempus...</h3>
<h3 class="abs article-title" style="left:791px;font-weight:400">Vestibulum placerat ultricies elit eget interdum, duis tristique faucibus...</h3>
<div class="abs article-more label" style="left:130px">Read More</div>
<div class="abs article-more label" style="left:459px">Read More</div>
<div class="abs article-more label" style="left:791px">Read More</div>

<!-- Follow -->
<h2 class="abs section-title script" style="top:3898px">Follow #Velour Hollis</h2>
<div class="photo insta" style="left:0;width:250px;background:linear-gradient(135deg,#e9e2dc,#b48a6c 60%,#e8e0d9)" role="img" aria-label="Woman making a heart shape with her hands"></div>
<div class="photo insta" style="left:250px;width:252px;background:linear-gradient(180deg,#4a4444,#7c6a46 55%,#c9a43a)" role="img" aria-label="Woman holding a red heart in front of her face"></div>
<div class="photo insta" style="left:502px;width:254px;background:linear-gradient(180deg,#ececec,#d8c9bd 55%,#e6a08a)" role="img" aria-label="Woman jumping in a white top and coral shorts"></div>
<div class="photo insta" style="left:756px;width:254px;background:linear-gradient(135deg,#e7ded6,#a07a5c 55%,#e4dbd3)" role="img" aria-label="Portrait of a woman with long wavy hair"></div>
<div class="photo insta" style="left:1010px;width:190px;background:linear-gradient(180deg,#f1ece6,#c39a7c 50%,#e7b62a)" role="img" aria-label="Laughing woman in a yellow top"></div>

<!-- Footer -->
<div class="abs footer-band"></div>
<div class="abs foot-brand">
  <div class="mark"></div>
  <div class="name">Velour Hollis</div>
  <div class="tag">LUXURY LIFESTYLE</div>
</div>
<p class="abs foot-text" style="top:4458px;left:156px;width:220px">Suite 12, Linden Row 4, Marbrook Quarter, Eastvale</p>
<div class="abs foot-text contact" style="top:4515px;left:152px">
  <span class="dot"><svg width="10" height="8" viewBox="0 0 10 8"><rect x="0.5" y="0.5" width="9" height="7" fill="none" stroke="#2f3a3a"/><polyline points="0.5,0.5 5,4.5 9.5,0.5" fill="none" stroke="#2f3a3a"/></svg></span>hello@velourhollis.com
</div>
<div class="abs foot-text contact" style="top:4548px;left:152px">
  <span class="dot"><svg width="10" height="10" viewBox="0 0 10 10"><path d="M2 1 L4 3 L3 4.5 Q4.5 6 5.5 7 L7 6 L9 8 L7.5 9.5 Q3 8.5 0.5 2.5 Z" fill="#2f3a3a"/></svg></span>555-310-0187
</div>

<div class="abs foot-head" style="top:4372px;left:496px">Company</div>
<ul class="abs foot-links">
  <li>Home</li><li>About</li><li>Lifestyle</li><li>Shop</li><li>Outfits</li><li>Videos</li><li>Contact</li>
</ul>

<div class="abs foot-head" style="top:4370px;left:749px">Don’t miss out!</div>
<p class="abs foot-text" style="top:4414px;left:749px;width:330px;font-size:11px;line-height:20px">We Don’t Keep Our fashion and tastes Secrets please Subscribe now &amp; thank us later</p>
<div class="abs email">Your email address</div>
<div class="btn" style="top:4474px;left:1000px;width:101px;height:44px;font-size:11px;letter-spacing:1px">Let’s Go</div>
<div class="abs foot-head" style="top:4546px;left:749px">Connect with us</div>
<div class="abs social"><span></span><span></span><span></span></div>

<div class="abs copyright">Copyright © 2023 Velour Hollis . All rights reserved</div>

</body>
</html>
```